Australian small vineyard seeking wine label.

We need a wine label design for a new wine brand \Boutique winery - 2 vintages so far, looking for something a little eye catching, but simple.
Wine label name: Brent and Co
2013 Cabernet Shiraz
2014 Shiraz
Estate grown
Vineyard located at Sevenhill in the Clare valley South Australia.

Target Market(s)

ladies aged between 20 and 50

Industry/Entity Type

Boutique

Logo Text

Brent and Co

Logo styles of interest
Emblem Logo
Pictorial/Combination Logo
Abstract Logo
Character Logo
Font styles to use
Serif
Script

Requirements
Must have
• easy to read text
Nice to have
• The grape grower and winemaker is Martin Brent -
• had some thoughts of Captain Brent - Australian - naval flag
• But very open to ideas
Should not have
• over complications and colors due to cost of wine label being determined by amount of colors required abd print set up.

```html
<!DOCTYPE html>
<html lang="en">
<head>
<meta charset="utf-8">
<title>Brent and Co — 2013 Cabernet Shiraz Label</title>
<link rel="stylesheet" href="https://fonts.googleapis.com/css2?family=Playfair+Display:wght@400&family=Libre+Baskerville&family=Pinyon+Script&family=Montserrat:wght@400&display=swap">
<style>
  :root {
    --backdrop: #2a2a2a;
    --label-light: #efede3;
    --label-mid: #e3e0d2;
    --label-edge: #d2cebd;
    --ink: #2b2a27;
    --ink-soft: #4a4843;
    --portrait-light: #cfcbbb;
    --portrait-dark: #5e5b53;
  }
  html, body {
    margin: 0;
    padding: 0;
    width: 684px;
    height: 1200px;
    overflow: hidden;
    background: var(--backdrop);
  }
  .canvas {
    position: relative;
    width: 684px;
    height: 1200px;
  }
  .wine-label {
    position: absolute;
    left: 94px;
    top: 230px;
    width: 496px;
    height: 740px;
    background: linear-gradient(90deg, var(--label-edge) 0%, var(--label-mid) 12%, var(--label-light) 45%, var(--label-mid) 85%, var(--label-edge) 100%);
    color: var(--ink);
    text-align: center;
  }
  .brand-name {
    position: absolute;
    top: 72px;
    left: 0;
    right: 0;
    margin: 0;
    font-family: "Playfair Display", serif;
    font-weight: 400;
    font-size: 50px;
    letter-spacing: 0.5px;
    color: var(--ink);
  }
  .portrait {
    position: absolute;
    top: 160px;
    left: 158px;
    width: 180px;
    height: 290px;
    background: radial-gradient(ellipse at 50% 35%, var(--portrait-light) 0%, var(--portrait-dark) 100%);
    border-radius: 2px;
  }
  .vintage {
    position: absolute;
    top: 512px;
    left: 0;
    right: 0;
    font-family: "Libre Baskerville", serif;
    font-size: 17px;
    letter-spacing: 2px;
    color: var(--ink-soft);
  }
  .varietal {
    position: absolute;
    top: 540px;
    left: 0;
    right: 0;
    font-family: "Libre Baskerville", serif;
    font-size: 27px;
    letter-spacing: 4px;
    color: var(--ink);
  }
  .region {
    position: absolute;
    top: 628px;
    left: 0;
    right: 0;
    font-family: "Pinyon Script", cursive;
    font-size: 40px;
    color: var(--ink);
  }
  .state {
    position: absolute;
    top: 690px;
    left: 0;
    right: 0;
    font-family: "Montserrat", sans-serif;
    font-size: 12px;
    letter-spacing: 5px;
    color: var(--ink-soft);
  }
</style>
</head>
<body>
  <div class="canvas">
    <section class="wine-label">
      <h1 class="brand-name">Brent and Co</h1>
      <div class="portrait" role="img" aria-label="Engraved portrait of Captain Brent in naval coat"></div>
      <div class="vintage">2013</div>
      <div class="varietal">CABERNET SHIRAZ</div>
      <div class="region">Clare Valley</div>
      <div class="state">SOUTH AUSTRALIA</div>
    </section>
  </div>
</body>
</html>
```